Update Old OR create new Website

Current Website is looking a bit old, I did this one a few years back.

Would like a fresh new look, current website sitepress theme is " the Vanta theme" from plumcrate and I just purchased this theme - "bravlo" also from plumcrate, I quite like the look of - http://bravlo.quorvex-skins.com/tech-business/ and if we could get somthing simlar would be great.

current website is at http://www.hle.com.au, have been playing around with the slider that i like.

I have said 5 pages to be designed but really it is just a 5 page website where most pages will look the same.

Any questions please let me know

Target Market(s)

Business

Coding

Coded - Design and coding required

Number of Pages Required

5+ page

Font styles to use
Sans Serif

Colors
33a6d7
0292cd
ffffff
0255a3

Requirements
Must have
• Device compatibility - pc, tablet, phone
Nice to have
• video
Should not have
• vunerabilities. Must also use images that will expire or disappear, ie must be uploaded to site not links to elsewhere.

```html
<!DOCTYPE html>
<html lang="en">
<head>
<meta charset="utf-8">
<title>Halden Technologies — Whatever IT takes</title>
<link href="https://fonts.googleapis.com/css2?family=Poppins:wght@400;500;600;700&family=Open+Sans:wght@400;600&display=swap" rel="stylesheet">
<style>
:root{
  --blue:#33a6d7;
  --blue-deep:#0292cd;
  --navy-blue:#0255a3;
  --white:#ffffff;
  --ink:#22262e;
  --text:#6d7480;
  --muted:#9aa1ab;
  --line:#e6e9ee;
  --light:#f4f5f7;
  --dark:#1f2630;
  --darker:#171c24;
  --hero:#0b1230;
}
*{box-sizing:border-box;margin:0;padding:0}
html,body{width:1200px;height:4108px;overflow:hidden}
body{font-family:"Open Sans",Arial,sans-serif;color:var(--text);background:var(--white);font-size:13px;line-height:1.7}
h1,h2,h3,h4,.btn,.nav a,.brand{font-family:"Poppins",Arial,sans-serif}
section,header,footer{position:relative;width:1200px}
.btn{display:inline-block;font-size:11px;font-weight:600;letter-spacing:.5px;padding:10px 22px;border-radius:3px;text-transform:uppercase}
.btn-white{background:var(--white);color:var(--ink)}
.btn-outline{border:1px solid var(--white);color:var(--white)}
.btn-dark-outline{border:1px solid #c9ced6;color:var(--ink);background:var(--white)}

/* top bar */
.topbar{height:32px;background:var(--darker);display:flex;align-items:center;padding:0 0 0 88px;color:#c7ccd4;font-size:11px}
.topbar .follow{display:flex;gap:6px;align-items:center}
.dot{width:12px;height:12px;border-radius:50%;background:#4a5260;display:inline-block}
.topbar .mail{margin-left:auto;margin-right:24px}
.topbar .call{background:var(--blue);color:var(--white);height:32px;line-height:32px;padding:0 28px;font-weight:600;margin-right:88px}

/* header */
.site-header{height:96px;display:flex;align-items:center;padding:0 88px;border-bottom:1px solid var(--line)}
.brand{display:flex;align-items:center;gap:10px;font-weight:600;color:var(--navy-blue);font-size:20px}
.brand .sq{width:26px;height:26px;background:var(--blue)}
.nav{margin-left:auto;display:flex;gap:30px;align-items:center}
.nav a{font-size:12px;font-weight:500;color:var(--ink);text-decoration:none}
.nav a.active{color:var(--blue)}

/* hero */
.hero{height:512px;background:radial-gradient(ellipse at 20% 70%,#1d6fd1 0%,#0c2a6a 35%,var(--hero) 70%);overflow:hidden;text-align:center;color:var(--white)}
.hero-glow{position:absolute;inset:0}
.hero h1{position:relative;padding-top:96px;font-size:56px;font-weight:700;letter-spacing:1px}
.hero h1 span{color:var(--blue)}
.hero p{position:relative;font-size:14px;margin:8px 0 26px}
.hero .btn{position:relative}
.hero-curve{position:absolute;bottom:0;left:0}
.scroll-down{position:absolute;bottom:14px;left:584px;width:32px;height:32px;border-radius:50%;border:2px solid #9aa1ab;background:var(--white)}

/* services */
.services{height:500px;text-align:center}
.section-title{font-size:30px;font-weight:600;color:var(--ink)}
.services .section-title{padding-top:80px}
.service-cards{position:absolute;top:144px;left:88px;display:flex;gap:28px}
.service-card{width:324px;height:316px;border:1px solid var(--line);padding:34px 36px;box-shadow:0 2px 12px rgba(0,0,0,.05)}
.service-card h3{font-size:18px;font-weight:500;color:var(--ink);margin:14px 0 10px}
.service-card p{font-size:12px;line-height:1.8}
.service-card .btn{margin-top:20px;border:1px solid var(--line);color:var(--ink)}
.service-card.featured{background:var(--blue);color:var(--white);border-color:var(--blue);height:316px}
.service-card.featured h3{color:var(--white)}
.service-card.featured .btn{background:var(--white)}

/* support */
.support{height:428px;background:var(--light);margin-top:40px}
.support-photo{position:absolute;left:110px;top:40px;width:300px;height:348px;border-radius:4px;background:linear-gradient(160deg,#e9ebee,#c9b7a6)}
.support-copy{position:absolute;left:480px;top:86px;width:600px}
.support-copy .eyebrow{font-size:13px;color:var(--ink)}
.support-copy h2{font-size:32px;font-weight:600;color:var(--ink);line-height:1.25;margin-bottom:14px}
.support-copy p{font-size:12px;margin-bottom:22px}

/* pricing */
.pricing{height:688px;background:linear-gradient(180deg,#2b323d,var(--dark));color:var(--white);text-align:center}
.pricing .section-title{color:var(--white);padding-top:60px}
.pricing .lead{font-size:12px;color:#b8bec7;width:560px;margin:6px auto 22px}
.toggle{display:flex;justify-content:center;gap:6px}
.toggle .btn{background:var(--white);color:var(--ink);padding:10px 26px}
.toggle .btn.off{background:transparent;border:1px solid #7b838f;color:var(--white)}
.slider{position:absolute;top:286px;left:110px;width:980px;height:4px;background:#59616d}
.slider .fill{width:270px;height:4px;background:var(--blue)}
.slider .knob{position:absolute;left:260px;top:-9px;width:22px;height:22px;border-radius:50%;background:var(--blue);border:4px solid var(--white)}
.price-card{position:absolute;top:328px;left:440px;width:320px;height:320px;background:var(--white);color:var(--text);padding:34px 30px}
.price-card h3{font-size:20px;color:var(--ink);font-weight:500}
.price-card p{font-size:11px;margin:6px 0 12px}
.price-card .amount{display:inline-block;background:var(--blue);color:var(--white);font-family:"Poppins",Arial,sans-serif;font-size:36px;font-weight:600;padding:4px 22px;border-radius:4px}
.price-card .per{font-size:11px;color:var(--muted);margin-left:6px}
.price-card .btn{margin-top:26px;border:1px solid var(--line);color:var(--ink)}

/* process */
.process{height:532px}
.process .section-title{position:absolute;left:88px;top:62px}
.step{position:absolute;left:88px;width:520px;display:flex;gap:18px}
.step .ic{width:44px;height:44px;border-radius:50%;background:var(--blue);flex:none}
.step h4{font-size:15px;color:var(--ink);font-weight:500}
.step p{font-size:12px}
.devices{position:absolute;left:640px;top:112px;width:480px;height:320px;background:linear-gradient(135deg,#eef2f6,#c8d2dc)}

/* cta */
.cta{height:320px;background:var(--blue);color:var(--white);text-align:center}
.cta h2{padding-top:82px;font-size:30px;font-weight:600}
.cta p{width:720px;margin:8px auto 26px;font-size:12px}
.cta .btn{margin:0 4px}
.cta .btn-white{color:var(--ink)}

/* testimonials */
.testimonials{height:560px;text-align:center}
.testimonials .section-title{padding-top:82px}
.quotes{position:absolute;top:152px;left:88px;display:flex;gap:20px}
.quote{width:328px;height:208px;border:1px solid var(--line);padding:56px 26px 20px;font-size:12px;position:relative}
.quote.mid{box-shadow:0 4px 18px rgba(0,0,0,.08)}
.avatar{position:absolute;top:-30px;left:134px;width:58px;height:58px;border-radius:50%;background:linear-gradient(135deg,#d8c6b8,#8b7566);border:3px solid var(--white)}
.quote .who{margin-top:10px;font-size:11px;color:var(--muted)}
.quote .who b{color:var(--blue);font-weight:600}
.clients{position:absolute;top:432px;left:88px;width:1024px;display:flex;justify-content:space-between}
.client{width:180px;height:82px;border:1px solid var(--line);display:flex;align-items:center;justify-content:center;gap:8px;font-family:"Poppins",Arial,sans-serif;font-size:16px;font-weight:600;color:#8a929c}
.client i{width:14px;height:14px;background:#c3c9d0}

/* footer */
.site-footer{height:436px;background:var(--dark);color:#aab1bb}
.footer-cols{position:absolute;top:48px;left:88px;display:flex}
.footer-col{width:256px;font-size:11px;line-height:2.1}
.footer-col h4{color:var(--white);font-size:14px;font-weight:500;margin-bottom:12px}
.contact-line{display:flex;gap:8px;align-items:center}
.contact-line svg{flex:none}
.subscribe{display:flex;margin:12px 0 26px}
.subscribe .field{width:232px;height:34px;background:var(--white);color:var(--muted);padding:0 12px;line-height:34px}
.subscribe .go{width:34px;height:34px;background:var(--blue)}
.socials{display:flex;gap:8px;margin-top:8px}
.socials .dot{width:26px;height:26px;background:#3a424e}
.copyright{position:absolute;bottom:0;left:0;width:1200px;height:48px;line-height:48px;text-align:center;background:var(--darker);font-size:11px}
.to-top{position:absolute;right:32px;bottom:64px;width:34px;height:34px;border-radius:50%;background:var(--blue)}
</style>
</head>
<body>

<div class="topbar">
  <div class="follow">Follow Us <span class="dot"></span><span class="dot"></span><span class="dot"></span><span class="dot"></span></div>
  <div class="mail">hello@haldentech.com.au</div>
  <div class="call">CALL NOW! 1 800 555 014</div>
</div>

<header class="site-header">
  <div class="brand"><span class="sq"></span>Halden Technologies</div>
  <nav class="nav">
    <a class="active">HOME</a><a>SERVICES</a><a>NETWORKS</a><a>MANAGED IT</a><a>WEB</a><a>APPS</a><a>INTERNET</a><a>CONTACT</a>
    <svg width="16" height="16" viewBox="0 0 16 16"><circle cx="7" cy="7" r="5" fill="none" stroke="#22262e" stroke-width="2"/><path d="M11 11l4 4" stroke="#22262e" stroke-width="2"/></svg>
    <svg width="18" height="14" viewBox="0 0 18 14"><path d="M0 1h18M0 7h18M0 13h18" stroke="#22262e" stroke-width="2"/></svg>
  </nav>
</header>

<section class="hero">
  <div class="hero-glow" role="img" aria-label="Glowing blue digital particle wave across a dark background" style="background:radial-gradient(ellipse 60% 30% at 25% 75%,rgba(51,166,215,.55),transparent 70%),radial-gradient(ellipse 40% 25% at 85% 35%,rgba(51,166,215,.3),transparent 70%)"></div>
  <h1>Whatever <span>IT</span> takes</h1>
  <p>What would it take for your information systems to actually improve the performance of your organisation?</p>
  <span class="btn btn-white">Get in touch</span>
  <svg class="hero-curve" width="1200" height="60" viewBox="0 0 1200 60"><path d="M0 60V40Q300 10 600 30T1200 20V60Z" fill="#ffffff"/></svg>
  <div class="scroll-down"><svg width="28" height="28" viewBox="0 0 28 28"><path d="M9 12l5 5 5-5" fill="none" stroke="#22262e" stroke-width="2"/></svg></div>
</section>

<section class="services">
  <h2 class="section-title">Services We Provide</h2>
  <div class="service-cards">
    <article class="service-card">
      <svg width="44" height="44" viewBox="0 0 44 44"><rect x="6" y="4" width="32" height="10" rx="2" fill="none" stroke="#33a6d7" stroke-width="2"/><rect x="6" y="17" width="32" height="10" rx="2" fill="none" stroke="#33a6d7" stroke-width="2"/><rect x="6" y="30" width="32" height="10" rx="2" fill="none" stroke="#33a6d7" stroke-width="2"/><circle cx="32" cy="9" r="2" fill="#33a6d7"/><circle cx="32" cy="22" r="2" fill="#33a6d7"/><circle cx="32" cy="35" r="2" fill="#33a6d7"/></svg>
      <h3>Servers</h3>
      <p>Halden Technologies designs, installs and supports reliable server systems that keep your business data safe and available.</p>
      <span class="btn">Read more</span>
    </article>
    <article class="service-card">
      <svg width="44" height="44" viewBox="0 0 44 44"><circle cx="18" cy="14" r="8" fill="none" stroke="#33a6d7" stroke-width="2"/><path d="M4 40c0-10 6-15 14-15s14 5 14 15" fill="none" stroke="#33a6d7" stroke-width="2"/><circle cx="34" cy="30" r="6" fill="none" stroke="#33a6d7" stroke-width="2"/></svg>
      <h3>Managed IT</h3>
      <p>Clients of all industries entrust Halden Technologies for ongoing IT support, monitoring and planning of their systems.</p>
      <span class="btn">Read more</span>
    </article>
    <article class="service-card featured">
      <svg width="44" height="44" viewBox="0 0 44 44"><circle cx="22" cy="26" r="3" fill="#fff"/><path d="M14 18a11 11 0 0 0 0 16M30 18a11 11 0 0 1 0 16M8 12a19 19 0 0 0 0 28M36 12a19 19 0 0 1 0 28" fill="none" stroke="#fff" stroke-width="2"/></svg>
      <h3>Internet Solutions</h3>
      <p>Halden Technologies is a wholesale provider of fast, secure connectivity for businesses of any size across the region.</p>
      <span class="btn btn-white">Read more</span>
    </article>
  </div>
</section>

<section class="support">
  <div class="support-photo" role="img" aria-label="Photo of a support agent wearing a headset"></div>
  <div class="support-copy">
    <div class="eyebrow">Need Your Help?</div>
    <h2>Our 5-Star Support Will Help You.</h2>
    <p>Our friendly support desk answers quickly and fixes problems properly. Whether it is a single laptop or your whole network, our team works with you until everything runs smoothly again, with clear advice and no jargon along the way.</p>
    <span class="btn btn-dark-outline">Contact us</span>
  </div>
</section>

<section class="pricing">
  <h2 class="section-title">Calculate the cost for Service</h2>
  <p class="lead">Choose the number of users and devices you need supported and see an estimated monthly cost instantly.</p>
  <div class="toggle"><span class="btn">Monthly pricing</span><span class="btn off">Yearly pricing</span></div>
  <div class="slider"><div class="fill"></div><div class="knob"></div></div>
  <div class="price-card">
    <h3>Premium</h3>
    <p>Full support for growing teams, including monitoring, backups and on-site visits.</p>
    <span class="amount">$210</span><span class="per">/month</span><br>
    <span class="btn">Free trial</span>
  </div>
</section>

<section class="process">
  <h2 class="section-title">How we do it</h2>
  <div class="step" style="top:136px"><span class="ic"></span><div><h4>Step 1</h4><p>We listen to how your business works and review the systems you already have in place.</p></div></div>
  <div class="step" style="top:236px"><span class="ic"></span><div><h4>Step 2</h4><p>We design a practical plan that fits your budget, goals and timeframe.</p></div></div>
  <div class="step" style="top:336px"><span class="ic"></span><div><h4>Step 3</h4><p>We set everything up, train your staff and keep supporting you afterwards.</p></div></div>
  <div class="devices" role="img" aria-label="Illustration of a desktop, laptop, tablet and phone showing the website"></div>
</section>

<section class="cta">
  <h2>Use Halden Technologies for any Business, Start Today!</h2>
  <p>From small offices to multi-site companies, we provide dependable IT, networks and internet so you can focus on running your business.</p>
  <span class="btn btn-white">Learn more</span><span class="btn btn-outline">Buy the theme</span>
</section>

<section class="testimonials">
  <h2 class="section-title">Client's Testimonials</h2>
  <div class="quotes">
    <div class="quote"><span class="avatar" role="img" aria-label="Client portrait"></span>Quick responses and honest advice every time. Our office network has never run better.<div class="who"><b>Jenna Marsh</b> - General Manager</div></div>
    <div class="quote mid"><span class="avatar" role="img" aria-label="Client portrait"></span>They moved our whole team to new servers over a weekend with zero downtime.<div class="who"><b>Clara Holt</b> - General Manager</div></div>
    <div class="quote"><span class="avatar" role="img" aria-label="Client portrait"></span>Friendly people who explain things clearly and always follow through.<div class="who"><b>Owen Pratt</b> - General Manager</div></div>
  </div>
  <div class="clients">
    <div class="client"><i></i>Norvik</div>
    <div class="client"><i></i>Pellham</div>
    <div class="client"><i></i>Tandora</div>
    <div class="client"><i></i>Quillfy</div>
    <div class="client"><i></i>Ostrel</div>
  </div>
</section>

<footer class="site-footer">
  <div class="footer-cols">
    <div class="footer-col"><h4>Quick Links</h4>Home<br>Services<br>Networks<br>Managed IT<br>Web<br>Apps<br>Internet<br>Contact</div>
    <div class="footer-col"><h4>Services</h4>Site Map<br>Terms &amp; Condition<br>Privacy Policy<br>FAQ's<br>Evaluation Services<br>Guidelines<br>News<br>Support</div>
    <div class="footer-col"><h4>Contact Details</h4>
      <div class="contact-line"><svg width="12" height="14" viewBox="0 0 12 14"><path d="M6 13S1 8 1 5a5 5 0 0 1 10 0c0 3-5 8-5 8z" fill="#33a6d7"/></svg>Suite 4, 12 Harbour Lane, Bayside</div>
      <div class="contact-line"><svg width="12" height="12" viewBox="0 0 12 12"><path d="M2 1l3 0 1 3-2 1a7 7 0 0 0 3 3l1-2 3 1v3c-6 0-10-4-10-9z" fill="#33a6d7"/></svg>(03) 5550 1420</div>
      <div class="contact-line"><svg width="12" height="10" viewBox="0 0 12 10"><rect x="0.5" y="0.5" width="11" height="9" fill="none" stroke="#33a6d7"/><path d="M1 1l5 4 5-4" fill="none" stroke="#33a6d7"/></svg>hello@haldentech.com.au</div>
      <div class="contact-line"><svg width="12" height="12" viewBox="0 0 12 12"><path d="M2 1l3 0 1 3-2 1a7 7 0 0 0 3 3l1-2 3 1v3c-6 0-10-4-10-9z" fill="#33a6d7"/></svg>(03) 5550 1488</div>
    </div>
    <div class="footer-col" style="width:300px"><h4>Subscribe Newsletter</h4>Subscribe to our newsletter for the latest updates and offers.
      <div class="subscribe"><div class="field">Enter email</div><div class="go"></div></div>
      <h4>Follow us</h4>
      <div class="socials"><span class="dot"></span><span class="dot"></span><span class="dot"></span><span class="dot"></span><span class="dot"></span></div>
    </div>
  </div>
  <div class="to-top"></div>
  <div class="copyright">Copyright © 2017, Halden Technologies. All rights reserved.</div>
</footer>

</body>
</html>
```